Kolibri-Stube
Ich bin sehr zufrieden mit dem Flyer, Plakat und Logo, welches ich für einen zahlbaren Preis bekommen habe. quorvix hat die Korrekturvorschläge sehr gut und immer zügig umgesetzt und ein wirklich gelungenes Resultat produzier.
Zielgruppe
Logo/Sloagan: Kolibri-Stube
Branchen: Kunst/Kultur und Bildung
Ich biete eine Kolibri-Stube an, in der bis 12 Personen quartalsweise über ein Jahr hinweg an einer Erzählung ode einem Roman arbeiten. Das Genre kann frei gewählt werden. Ob Kriminal-, Fantasy oder Liebesroman, Autobiografie oder Dokufiktion, die Grundlagen eines spannenden Textes sind die selben.
Zielgruppe sind Jugendliche bis Senioren, die gerne eine lägere Erzählung oder einen Roman schreiben möchten.
Aufgabenstellung
Siehe Design-Briefing (PDF) mit Inhalt für Flyertext
Wichtig ist mir der Flyer A4 gefaltet (zu A5 oder 2x gefaltet) oder A5, alle beidseits bedruckt und je nachdem, wie sie den Inhalt verteilen möchten.
Ich bin offen für Design- und Formatvorschläge.
- Ein Plakat A4/A3, welches mit der Vorderseite des Flyers grösstenteils übereinstimmt. Wenn ich ein InDesign oder Photoshop mit Layern kriege, kann ich den Text des Plakats selber ergänzen/bearbeiten.
Ich habe neben dem Briefing und einem Foto von mir noch ein paar Bilder hochgeladen, deren Stil mir gefällt. Habe aber NICHT deren Rechte. Bilder müssten also durch Sie gefunden werden, ich kann diese aber extra bezahlen, bitte Preis dafür deklarieren.
Logo brauche ich noch keines.
Besten Dank für Ihre Bemühungen

```html
<!DOCTYPE html>
<html lang="de">
<head>
<meta charset="utf-8">
<title>Kolibri-Stube – Flyer</title>
<link href="https://fonts.googleapis.com/css2?family=Encode+Sans+Condensed:wght@300;400;600;700&display=swap" rel="stylesheet">
<style>
  :root {
    --maroon-deep: #460000;
    --maroon-mid: #7a0000;
    --maroon-light: #8c1616;
    --headline-red: #730808;
    --gold: #f0c20a;
    --paper: #ffffff;
    --blush: #e2c0c0;
    --ink: #1a1a1a;
  }
  * { box-sizing: border-box; margin: 0; padding: 0; }
  html, body { width: 849px; height: 1200px; overflow: hidden; background: var(--paper); }
  body { font-family: "Encode Sans Condensed", "Arial Narrow", sans-serif; color: var(--ink); }
  .sheet { position: relative; width: 849px; height: 1200px; overflow: hidden; }
  .backdrop { position: absolute; inset: 0; }
  .fold-line { position: absolute; left: 423.5px; width: 1px; background: rgba(0,0,0,.35); }
  .fold-top { top: 0; height: 598px; }
  .fold-bottom { top: 603px; height: 597px; }

  .corner { position: absolute; width: 50px; height: 50px; }

  .claim {
    position: absolute; left: 40px; width: 356px; top: 88px;
    text-align: center; color: var(--headline-red); line-height: 71px;
    font-size: 56px; font-weight: 300;
  }
  .claim strong { font-weight: 700; font-size: 58px; }

  .brand-card {
    position: absolute; left: 465px; top: 47px; width: 221px; height: 336px;
    background: var(--paper); border: 1px solid #000;
  }
  .brand-name {
    position: absolute; left: 22px; top: 26px; width: 180px;
    font-size: 50px; font-weight: 600; line-height: 60px; letter-spacing: 3px; color: #000;
  }
  .quill {
    position: absolute; left: 623px; top: 232px; width: 195px; height: 140px;
    background: radial-gradient(ellipse at 60% 40%, #f0c20a 0%, #e6b400 60%, rgba(240,194,10,0) 72%);
  }
  .tagline {
    position: absolute; color: var(--paper); font-size: 21px; font-weight: 400; line-height: 27px;
  }
  .tagline-one { left: 522px; top: 402px; }
  .tagline-two { left: 553px; top: 429px; }
  .site-front { position: absolute; left: 464px; top: 545px; color: var(--paper); font-size: 20px; }

  .box { position: absolute; left: 89px; width: 229px; padding: 0 5px; }
  .box-white { background: var(--paper); }
  .box-blush { background: var(--blush); }
  .box-right { left: 541px; }
  .question { font-size: 12.4px; line-height: 16.2px; font-weight: 300; padding: 0 7px; }
  .question p { margin-bottom: 12px; }
  .question b { font-weight: 600; }
  .small { font-size: 8.6px; line-height: 12px; font-weight: 300; text-align: justify; }
  .signature { font-size: 5.5px; margin-top: 4px; }
  .topics { font-size: 9.2px; line-height: 12.1px; font-weight: 300; padding: 4px 5px; }
  .topics ul { list-style: none; margin-top: 12px; }
  .topics li::before { content: "·"; display: inline-block; width: 8px; }
  .site-back { position: absolute; left: 542px; top: 1005px; color: var(--paper); font-size: 24px; font-weight: 300; }
  .quill-faint {
    position: absolute; left: 445px; top: 955px; width: 360px; height: 150px;
    background: radial-gradient(ellipse at 55% 45%, rgba(240,194,10,.12) 0%, rgba(240,194,10,0) 70%);
  }
</style>
</head>
<body>
<div class="sheet">
  <svg class="backdrop" width="849" height="1200" viewBox="0 0 849 1200" aria-hidden="true">
    <rect width="849" height="1200" fill="var(--maroon-deep)"/>
    <!-- top left panel -->
    <polygon points="0,90 72,162 72,598 0,598" fill="var(--maroon-light)"/>
    <polygon points="0,325 72,397 72,598 0,598" fill="var(--maroon-mid)"/>
    <polygon points="362,452 424,514 424,598 362,598" fill="var(--maroon-light)"/>
    <!-- top right panel -->
    <polygon points="424,250 560,250 849,540 849,598 424,598" fill="var(--maroon-deep)"/>
    <polygon points="686,47 849,210 849,598 760,598 465,383 686,383" fill="var(--maroon-light)"/>
    <polygon points="465,383 686,383 849,546 849,598 680,598" fill="var(--maroon-mid)"/>
    <polygon points="560,598 424,462 424,598" fill="var(--maroon-mid)"/>
    <!-- white divider -->
    <rect y="598" width="849" height="5" fill="var(--paper)"/>
    <!-- bottom left panel -->
    <polygon points="70,603 424,957 424,1200 0,1200 0,603" fill="var(--maroon-light)"/>
    <polygon points="0,900 300,1200 0,1200" fill="var(--maroon-mid)"/>
    <polygon points="0,603 70,603 424,957 424,1040 0,616" fill="var(--maroon-deep)" opacity=".0"/>
    <polygon points="0,1050 150,1200 0,1200" fill="var(--maroon-deep)"/>
    <polygon points="200,1130 270,1200 424,1200 424,1100 300,1130" fill="var(--maroon-mid)"/>
    <!-- bottom right panel -->
    <polygon points="424,603 849,603 849,700 424,1000" fill="var(--maroon-mid)"/>
    <polygon points="600,603 849,603 849,700" fill="var(--maroon-light)"/>
    <polygon points="424,1000 849,720 849,1200 424,1200" fill="var(--maroon-light)"/>
    <polygon points="424,1130 849,850 849,1000 600,1200 424,1200" fill="var(--maroon-mid)"/>
    <polygon points="424,900 520,850 520,1100 424,1130" fill="var(--maroon-deep)"/>
  </svg>

  <div class="fold-line fold-top"></div>
  <div class="fold-line fold-bottom"></div>

  <!-- corner lines -->
  <svg class="corner" style="left:78px;top:15px" viewBox="0 0 50 50" aria-hidden="true"><path d="M1,50 V14 Q1,1 14,1 H50" fill="none" stroke="var(--gold)" stroke-width="1.5"/></svg>
  <svg class="corner" style="left:290px;top:534px" viewBox="0 0 50 50" aria-hidden="true"><path d="M49,0 V36 Q49,49 36,49 H0" fill="none" stroke="var(--gold)" stroke-width="1.5"/></svg>
  <svg class="corner" style="left:784px;top:15px" viewBox="0 0 50 50" aria-hidden="true"><path d="M49,50 V14 Q49,1 36,1 H0" fill="none" stroke="var(--gold)" stroke-width="1.5"/></svg>
  <svg class="corner" style="left:439px;top:534px" viewBox="0 0 50 50" aria-hidden="true"><path d="M1,0 V36 Q1,49 14,49 H50" fill="none" stroke="var(--gold)" stroke-width="1.5"/></svg>
  <svg class="corner" style="left:78px;top:636px" viewBox="0 0 50 50" aria-hidden="true"><path d="M1,50 V14 Q1,1 14,1 H50" fill="none" stroke="var(--gold)" stroke-width="1.5"/></svg>
  <svg class="corner" style="left:732px;top:1114px" viewBox="0 0 50 50" aria-hidden="true"><path d="M49,0 V36 Q49,49 36,49 H0" fill="none" stroke="var(--gold)" stroke-width="1.5"/></svg>

  <!-- back cover -->
  <div class="claim">
    Ihr<br><strong>geistiger</strong><br><strong>Schatz</strong><br>in Form<br>eines<br><strong>Buches</strong>
  </div>

  <!-- front cover -->
  <div class="brand-card">
    <div class="brand-name">Kolibri-Stube</div>
  </div>
  <div class="quill" role="img" aria-label="Goldene Schreibfeder als Illustration"></div>
  <div class="tagline tagline-one">Mit der Kolibri-Stube</div>
  <div class="tagline tagline-two">zu Ihrem eigenen Roman</div>
  <div class="site-front">www.kolibri-stube.ch</div>

  <!-- inside left -->
  <div class="box box-white question" style="top:647px;height:250px;padding-top:36px">
    <p>Haben Sie eine erste <b>Idee</b> für<br>eine Erzählung oder einen Roman?</p>
    <p>Eine lebhafte <b>Fantasie</b> für das Ausserordentliche oder <b>ungewöhnlich Gewöhnliche?</b></p>
    <p>Oder ein <b>reiches Leben,</b> aus dessen Quelle Sie für Ihre Geschichte schöpfen können?</p>
    <p>Und möchten Sie den zukünftigen Leserinnen und Lesern <b>Ihren geistigen Schatz in Form eines Buches</b> schenken?</p>
  </div>
  <div class="box box-blush small" style="top:905px;height:54px;padding-top:2px">
    Dann schreiben Sie Ihren ersten eigenen Roman!<br>
    Ein erster Ideenfaden spinnt sich in Ihren Gedanken und vielleicht haben Sie diesen schon zu Papier gebracht. Aber Sie wissen nicht wie fortfahren?
  </div>
  <div class="box box-white question" style="top:968px;height:112px;padding-top:16px">
    Ich helfe Ihnen weiter!<br>
    Denn die <b>Schreibkunst fusst wie alle Künste nicht nur auf Genie, sondern in erster Linie auf Handwerk, dass Ich Ihnen beibringen kann.</b>
    <div class="signature">Dr. Lena Vorhold</div>
  </div>
  <div class="box box-blush small" style="top:1090px;height:65px;padding-top:4px">
    Sie selber lesen gerne und sind dem Schreiben nicht abgewandt. Eine perfekte Rechtschreibung ist nicht nötig, dafür gibt es das gegenseitige Lektorat. Aber sie sollten der deutschen Sprache soweit mächtig sein, dass Sie Haupt, Nebensätze, Fälle und Zeiten meistens korrekt anwenden.
  </div>

  <!-- inside right -->
  <div class="box box-right box-blush topics" style="top:647px;height:199px">
    Die Themen eines ganzen Jahres sind
    <ul>
      <li>Kreative Übungen für den Start des Schreibprozesses</li>
      <li>Schreibspiele, um Blockaden zu lösen</li>
      <li>Bestimmung des Genres und des Stils</li>
      <li>Entwicklung der Handlung und Spannung</li>
      <li>Wahl einer Erzählperspektive und der passenden Sprache</li>
      <li>Lebendige Protagonisten, Antagonisten und Nebenfiguren</li>
      <li>Dramatische Szenen durch Emotionen</li>
      <li>Gliederung des Stoffes zu einem roten Faden</li>
      <li>Lineare und nonlineare Erzählformen</li>
      <li>Eine Dreiaktstruktur mit interessanten Spannungsbögen</li>
      <li>Korrekturen des Stils und der Grammatik</li>
      <li>Stilistische, rhetorische und literarische Mittel</li>
      <li>Autobiografische Verfremdung und Wahrhaftigkeit</li>
      <li>Die Schnittmenge zwischen Leben und Fiktion</li>
    </ul>
  </div>
  <div class="box box-right box-blush small" style="top:855px;height:52px;padding-top:2px">
    Ein regelmässiger Austausch in Kleingruppen und im Plenum helfen Ihnen, Ihre Arbeit gegenseitig zu überdenken, zu korrigieren und zu erweitern. Verschiedene Textformen und exemplarische Beispiele aus der Literatur und dem Film bieten Impulse für den eigenen Text.
  </div>
  <div class="box box-right box-blush small" style="top:917px;height:30px;padding-top:3px">
    Ein eigener Laptop mit WLAN ist von Vorteil, da wir uns damit online leicht austauschen können.
  </div>
  <div class="quill-faint" role="img" aria-label="Zarte Federzeichnung als Hintergrunddekor"></div>
  <div class="site-back">www.kolibri-stube.ch</div>
  <div class="box box-right box-white small" style="top:1077px;height:92px;padding-top:3px">
    Kursleitung<br>
    <b style="font-weight:600">Dr. Lena Vorhold</b> ist Erwachsenenbildnerin und Lehrerin für Deutsch und spezialisierte sich auf den Unterricht des literarischen Schreibens von Drehbücher, Erzählungen und Romanen. Als Autorin mehrerer Fachbücher und Verlagsleiterin des Talmon Verlags kennt Sie auch die Möglichkeiten des Vertriebes und Buchhandels.
  </div>
</div>
</body>
</html>
```